7K Ventures business cards for a tech VC

We're starting a new Venture Capital that is focusing on bringing the best start ups from Israel to NYC
We need a business cards template for this that gives the sense of an entrepreneurial look
I don't want any religious signs on this even thought it's Israel
I'm looking for a techi feeling but not too crazy
The card should probably be in the same light blue as the logo and the logo in white

Target Market(s)

Investors

Industry/Entity Type

Tech

Contact Information for Business Card

The card needs to look slick and entrepreneurship like
The VC is focused on NYC and Tel Aviv so could be great to show something on the back side that is like NYC skyline or something like that
You can see the logo attached

Colors
0455a3
3276b5
85acd3
cedeed
eaf1f7

Requirements
Must have
• A very cool looking business card that shows we're a cutting edge tech VC with a focus on bringing start ups from Tel Aviv and leveraging the NYC ecosystem
Nice to have
• NYC skyline can be cool , maybe something that is connected to Tel Aviv

```html
<!DOCTYPE html>
<html lang="en">
<head>
<meta charset="utf-8">
<title>7K Ventures – Business Card</title>
<link href="https://fonts.googleapis.com/css2?family=Open+Sans:wght@400;600;700&display=swap" rel="stylesheet">
<style>
  :root {
    --bg: #2a2a2a;
    --brand-blue: #1b8fd0;
    --card-white: #ffffff;
    --text-dark: #3a3a3a;
    --text-muted: #555555;
    --divider: #9cc7e6;
  }
  * { box-sizing: border-box; margin: 0; padding: 0; }
  html, body { width: 1200px; height: 1200px; overflow: hidden; }
  body {
    background: var(--bg);
    font-family: "Open Sans", Arial, sans-serif;
    display: flex;
    flex-direction: column;
    align-items: center;
    justify-content: center;
    gap: 52px;
  }
  .card {
    width: 900px;
    height: 514px;
    border-radius: 4px;
    position: relative;
    box-shadow: 0 6px 18px rgba(0,0,0,0.35);
  }
  .card-front {
    background: var(--brand-blue);
    display: flex;
    align-items: center;
    justify-content: center;
  }
  .brand-name {
    font-weight: 700;
    letter-spacing: 2px;
    text-transform: uppercase;
    line-height: 1;
  }
  .card-front .brand-name { color: var(--card-white); font-size: 64px; }
  .card-back {
    background: var(--card-white);
    display: flex;
    align-items: center;
  }
  .back-brand {
    width: 440px;
    display: flex;
    justify-content: center;
  }
  .card-back .brand-name { color: var(--brand-blue); font-size: 52px; }
  .divider {
    width: 1px;
    height: 300px;
    background: linear-gradient(to bottom, transparent, var(--divider) 20%, var(--divider) 80%, transparent);
  }
  .contact {
    padding-left: 44px;
    color: var(--text-dark);
  }
  .person-name {
    color: var(--brand-blue);
    font-weight: 600;
    font-size: 30px;
    letter-spacing: 0.5px;
    text-transform: uppercase;
  }
  .person-role { font-size: 18px; color: var(--text-muted); margin-bottom: 22px; }
  .contact-list { list-style: none; font-size: 19px; }
  .contact-list li {
    display: flex;
    align-items: flex-start;
    gap: 10px;
    line-height: 1.45;
  }
  .contact-list li.address { margin-top: 18px; }
  .icon { width: 16px; height: 16px; flex: none; margin-top: 6px; fill: var(--brand-blue); }
</style>
</head>
<body>
  <section class="card card-front">
    <span class="brand-name">7K Ventures</span>
  </section>

  <section class="card card-back">
    <div class="back-brand">
      <span class="brand-name">7K Ventures</span>
    </div>
    <div class="divider"></div>
    <div class="contact">
      <h1 class="person-name">Dana Levin</h1>
      <p class="person-role">Director</p>
      <ul class="contact-list">
        <li>
          <svg class="icon" viewBox="0 0 16 16" aria-hidden="true"><path d="M2 4c0-1 1-2 2-2h8c1 0 2 1 2 2v1h-3V4H5v1H2zM4 7h8l2 6H2z"/></svg>
          <span>1-555-014790</span>
        </li>
        <li>
          <svg class="icon" viewBox="0 0 16 16" aria-hidden="true"><circle cx="8" cy="8" r="6.5" fill="none" stroke="#1b8fd0" stroke-width="1.4"/><path d="M1.5 8h13M8 1.5c-3 3-3 10 0 13M8 1.5c3 3 3 10 0 13" fill="none" stroke="#1b8fd0" stroke-width="1.2"/></svg>
          <span>www.7kventures.com</span>
        </li>
        <li>
          <svg class="icon" viewBox="0 0 16 16" aria-hidden="true"><path d="M1 3h14v10H1z"/><path d="M1 3l7 6 7-6" fill="none" stroke="#fff" stroke-width="1.2"/></svg>
          <span>dana@7kventures.com</span>
        </li>
        <li class="address">
          <svg class="icon" viewBox="0 0 16 16" aria-hidden="true"><path d="M8 1l7 7h-2v7H9v-4H7v4H3V8H1z"/></svg>
          <span>Dummy city<br>Dummy Country Land</span>
        </li>
      </ul>
    </div>
  </section>
</body>
</html>
```